Zabrin Design Prize - $10,000 tablet app design contest, Brochure Category

Zabrin is a marketplace for iSlate App Templates (similar to PageForge templates). We want you to design an app template for sale in our marketplace which targets Brochure Apps (iSlate Apps for examples like travel brochure, university prospectus, music guide for a venue).

It’s up to you to create pages or features for the App Template that you think are appropriate. Creativity will be rewarded! Here are some example pages or features that you could create:

• Welcome page
• Guides to places, events etc.
• Maps - countries, local venue guide, university campuses etc.
• Contact page
• Hyperlinks to webpages
• Social media integration
• Animations and video

Your design should be Vibrant, Engaging and Contemporary. If you have an iSlate, download Zabrin Viewer and download template examples in the download tab.

Your entry must include:
• A brief description of your template
• Preview images of all pages of your template

Attached to this project are free templates to help you get started with your design. We have included:
1. A free portfolio template for designers/photographers
2. Icons and artwork to use in your template
3. Blank pages template
4. Form template
5. Video ad template

If you are selected as a finalist you will be required to submit an .zproject file containing:
• Your LayoutPro source files
• Preview images of your template
• All creative / stock assets used in the template (animations, video etc.)
• A text file with instructions on how to update the template
• A metadata .txt file containing template details and your information

How to enter:
1. Register at Marketplace and view the instructions under the welcome message https://marketplace.zabrinhub.example/welcome
2. Download Zabrin Editor: https://support.zabrinhub.example/entries/48150926-zabrin-editor
3. Use the free templates provided in this brief to create your designs and submit to PlanGather
Updates

Project Deadline Extended
Reason: Due to the Christmas break we are extending the deadline of our competition. Thank you for time and effort - I will be providing feedback over the next couple of days! Best wishes, Melika

Hi All,

I have received many screenshots with some great designs! I just wanted to clarify that you are designing Zabrin app templates including Zabrin features and not just page designs?

Read Tips for First Time Zabriners to guide you through the template creation process

Before you start designing templates for Zabrin Marketplace

·       Read the Quality Standards

·       Read the Copyright Information 

·       Use the Template Quality Checklist to ensure your template follows our guidelines. 

What should my project file contain?

·       A folder containing your source files, e.g. LayoutPro. This must be named Source.

·       The Zabrin content files. This must be named Bundle.

·       Instructions, explaining to a customer how to use your template.

Best wishes,

Melika

Project Deadline Extended
Reason: We are extending the competition by 7 days to give you more time!

Project Deadline Extended
Reason: We have received 3 complete designs for this contest so we are extending the deadline by 7 days. Melika :)

Target Market(s)

Entrepreneurs who wish to create iSlate Apps by using our App design templates.

Industry/Entity Type

University

Requirements
Must have
• You will need Zabrin Editor to open the .zproject files attached to this brief. Get it here: https://support.zabrinhub.example/entries/48150926-zabrin-editor
Should not have
• • Low quality, fuzzy or blurry images
• Any stock images or content which you do not own the rights to
• Any material which could be considered inappropriate or offensive

```html
<!DOCTYPE html>
<html lang="en">
<head>
<meta charset="utf-8">
<title>Scuba Diving – Brochure Page</title>
<link href="https://fonts.googleapis.com/css2?family=Oswald:wght@500&family=Roboto:wght@400;500&display=swap" rel="stylesheet">
<style>
  :root {
    --ocean-top: #3a8fc0;
    --ocean-mid: #1a6a9c;
    --ocean-deep: #0c4a72;
    --reef: #5b6a5a;
    --brand-orange: #f26a2e;
    --ink: #3d4a5c;
    --body-text: #2e3338;
    --white: #ffffff;
    --photo-a: #4d8a8f;
    --photo-b: #7a6048;
  }
  * { box-sizing: border-box; margin: 0; padding: 0; }
  html, body { width: 1200px; height: 900px; overflow: hidden; }
  body { position: relative; font-family: "Roboto", Arial, sans-serif; }

  .scene-backdrop {
    position: absolute; inset: 0;
    background:
      radial-gradient(ellipse 60% 40% at 30% 85%, rgba(150,140,70,.55), transparent 70%),
      linear-gradient(180deg, var(--ocean-top) 0%, var(--ocean-mid) 40%, var(--ocean-deep) 70%, var(--reef) 100%);
  }

  .brand-mark {
    position: absolute; left: 55px; top: 0; width: 141px; height: 88px;
    background: var(--brand-orange); color: var(--white);
    font-family: "Oswald", "Arial Narrow", sans-serif; font-weight: 500;
    font-size: 58px; line-height: 88px; text-align: center; letter-spacing: -1px;
  }

  .activity-card { position: absolute; left: 0; top: 0; width: 1200px; height: 900px; pointer-events: none; }
  .activity-card svg.card-shape { position: absolute; left: 0; top: 0; }

  .activity-icon { position: absolute; left: 633px; top: 93px; width: 68px; height: 68px; }

  .activity-title {
    position: absolute; left: 756px; top: 109px;
    font-size: 33px; font-weight: 400; color: var(--ink); line-height: 1;
  }

  .activity-photo {
    position: absolute; left: 755px; top: 177px; width: 315px; height: 362px;
    background: linear-gradient(160deg, var(--photo-a) 0%, #3a6f78 45%, var(--photo-b) 100%);
  }

  .activity-description {
    position: absolute; left: 755px; top: 570px; width: 320px;
    font-size: 13.4px; line-height: 20px; color: var(--body-text);
  }

  .share-links { position: absolute; left: 748px; top: 735px; display: flex; gap: 8px; }
  .share-links span {
    width: 33px; height: 33px; border-radius: 50%; background: var(--ink);
    display: flex; align-items: center; justify-content: center;
  }

  .book-button {
    position: absolute; left: 884px; top: 736px; width: 120px; height: 33px;
    border-radius: 17px; background: var(--ink); color: var(--white);
    font-size: 15px; font-weight: 500; letter-spacing: .3px;
    display: flex; align-items: center; justify-content: center;
  }

  .page-nav {
    position: absolute; top: 835px; width: 44px; height: 44px; border-radius: 50%;
    background: var(--ink); display: flex; align-items: center; justify-content: center;
  }
  .page-nav.prev { left: 33px; }
  .page-nav.next { left: 1124px; }
</style>
</head>
<body>
  <div class="scene-backdrop" role="img" aria-label="Underwater photo of a scuba diver with a camera above a coral reef and a school of yellow spotted fish"></div>

  <div class="brand-mark">LOGO</div>

  <div class="activity-card">
    <svg class="card-shape" width="1200" height="900" viewBox="0 0 1200 900" aria-hidden="true">
      <defs>
        <linearGradient id="cardFill" x1="0" y1="0" x2="0" y2="1">
          <stop offset="0" stop-color="#dfe8f0" stop-opacity=".8"/>
          <stop offset=".6" stop-color="#e9eef3" stop-opacity=".88"/>
          <stop offset="1" stop-color="#ffffff" stop-opacity=".97"/>
        </linearGradient>
      </defs>
      <path d="M636 83 H1103 Q1117 83 1117 97 V777 Q1117 791 1103 791 H723 Q709 791 709 777 V164 H636 Q622 164 622 150 V97 Q622 83 636 83 Z" fill="url(#cardFill)"/>
    </svg>

    <svg class="activity-icon" viewBox="0 0 68 68" aria-hidden="true">
      <circle cx="34" cy="34" r="34" fill="#3d4a5c"/>
      <rect x="17" y="26" width="34" height="15" rx="7" fill="none" stroke="#fff" stroke-width="3"/>
      <line x1="34" y1="28" x2="34" y2="39" stroke="#fff" stroke-width="2"/>
      <path d="M26 45 Q34 52 42 45" fill="none" stroke="#fff" stroke-width="3" stroke-linecap="round"/>
    </svg>

    <h1 class="activity-title">Scuba Diving</h1>

    <div class="activity-photo" role="img" aria-label="Photo of a snorkeller in a mask underwater surrounded by bubbles"></div>

    <p class="activity-description">Lorem ipsum dolor sit amet, consetetur sadip-scing elitr, sed diam nonumy eirmod tempor invidunt ut labore et dolore magna aliquyam erat, sed diam voluptua. At vero eos et accusam et justo duo dolores et ea rebum. Stet clita kasd gubergren, no sea takimata sanctus est Lorem ipsum dolor sit amet.</p>

    <div class="share-links">
      <span aria-label="Share"></span>
      <span aria-label="Share"></span>
      <span aria-label="Email">
        <svg width="17" height="12" viewBox="0 0 17 12" aria-hidden="true">
          <rect x="1" y="1" width="15" height="10" fill="none" stroke="#fff" stroke-width="1.6"/>
          <path d="M1 1 L8.5 7 L16 1" fill="none" stroke="#fff" stroke-width="1.6"/>
        </svg>
      </span>
    </div>

    <div class="book-button">BOOK NOW</div>
  </div>

  <div class="page-nav prev" aria-label="Previous page">
    <svg width="12" height="18" viewBox="0 0 12 18" aria-hidden="true"><path d="M9 2 L3 9 L9 16" fill="none" stroke="#fff" stroke-width="3"/></svg>
  </div>
  <div class="page-nav next" aria-label="Next page">
    <svg width="12" height="18" viewBox="0 0 12 18" aria-hidden="true"><path d="M3 2 L9 9 L3 16" fill="none" stroke="#fff" stroke-width="3"/></svg>
  </div>
</body>
</html>
```